Home page for local retail aggregator

About us: We are a new company that showcases beautiful products available at nearby retail stores. This homepage is meant to display the latest products featured on our site and also allow the user to search, browse with filters, and access their account details.

Currently, our home page looks a little bland. We want the focus of the site to remain on the featured photos and products but the design should be more cohesive. The most successful designs will make more subtle use of our colors, provide intuitive menu controls, and look visually stunning.

This homepage has a few sections:

Header:
-Top Section: will always remain at the top of the page. There should be space for our company name ”zAntelope”, a tagline, and a place for the menus.
-Menus: user must be able to find links for: “My profile” “My Products” “Add Product” “Preview store”
-Bottom section: this will scroll with the user and always remain at the top of the screen providing access to a search box, and filters for “location” “price” and retail categories.

Main Page:
-Each product featured is shown on a tile that includes a photo, title, price, name of store, has space to leave a comment, and include counters for "likes," comments, and "Pods"). “Pods” are bookmark folders. The user’s profile pic is also shown in miniature if they leave a comment.

The final version of the site must be delivered in a fully layered photoshop file and have versions demonstrating what the page will look like both when a user is logged-in and when logged-out.

Target Market(s)

Most of our users are female 18-45. Our customers are retail store owners who want their products to look attractive and professional.

Industry/Entity Type

Retail

Requirements
Must have
• Our logo must be present on the site (attached to project). You're welcome to change the colors in the header but it should look good with our logo.

For reference here are colors we're currently using:
Site text is in Dark Blue: RGB(10/23/47)
Logo color on business cards is light blue: (51/153/204)
Nice to have
• Would love to see new versions of the menus that are more modern and intuitive. Currently we just have links to each individual control. Putting these in a drop-down or re-arranging them would be nice.

```html
<!DOCTYPE html>
<html lang="en">
<head>
<meta charset="utf-8">
<title>zAntelope – Local product search and discovery</title>
<link rel="stylesheet" href="https://fonts.googleapis.com/css2?family=Open+Sans:wght@400;600;700;800&display=swap">
<style>
:root{
  --navy:#0a172f;
  --navy-mid:#16305a;
  --header-top:#0f2447;
  --header-bot:#1d3d6e;
  --brand-blue:#3399cc;
  --nav-bg:#b7c8de;
  --nav-text:#1b2e52;
  --banner-top:#2f5d9a;
  --banner-bot:#4a7ab7;
  --page-bg:#cdd9ea;
  --panel:#ffffff;
  --tile-border:#d6dde7;
  --muted:#8a93a3;
  --price:#9aa1ad;
  --input-border:#c7ced9;
  --footer-top:#1a355f;
  --footer-bot:#0f2244;
  --footer-text:#b9c8de;
}
*{box-sizing:border-box;margin:0;padding:0}
html,body{width:773px;height:1200px;overflow:hidden}
body{font-family:"Open Sans",Arial,sans-serif;color:var(--navy);background:linear-gradient(180deg,#dfe7f2 0%,var(--page-bg) 100%);position:relative}

/* Header */
.site-header{height:103px;background:linear-gradient(180deg,var(--header-top),var(--header-bot));position:relative}
.brand{position:absolute;left:40px;top:16px;display:flex;align-items:center;gap:12px}
.brand-mark{width:54px;height:54px;border-radius:50%;background:var(--brand-blue)}
.brand-name{font-size:27px;font-weight:700;color:#ffffff;line-height:1}
.brand-tagline{font-size:11px;color:#9fc3e6;margin-top:6px;font-weight:600}
.header-search{position:absolute;right:26px;top:38px;display:flex}
.header-search input{width:128px;height:30px;border:1px solid #8aa6cc;background:#ffffff;border-radius:2px 0 0 2px;font:inherit;font-size:11px;padding:0 8px}
.search-btn{width:32px;height:30px;background:var(--navy-mid);display:flex;align-items:center;justify-content:center;border-radius:0 2px 2px 0}

.main-nav{height:31px;background:linear-gradient(180deg,#cbd8e9,var(--nav-bg));margin:0 20px;display:flex;align-items:center;padding-left:14px;gap:4px;border-bottom:1px solid #9fb2cc}
.main-nav a{font-size:11px;font-weight:700;color:var(--nav-text);text-decoration:none;padding:0 16px}
.main-nav a.active{color:var(--brand-blue)}

.banner{margin:0 20px;height:98px;background:linear-gradient(180deg,var(--banner-top),var(--banner-bot));display:flex;align-items:center;justify-content:center}
.banner h1{font-size:19px;font-weight:700;color:#ffffff}

/* Product grid */
.product-panel{margin:0 21px;height:798px;background:var(--panel);border:1px solid #c4cfdf;padding:14px 19px 0 19px;display:grid;grid-template-columns:repeat(4,161px);grid-auto-rows:241px;column-gap:20px;row-gap:18px}
.tile{border:1px solid var(--tile-border);box-shadow:0 1px 3px rgba(10,23,47,.12);background:#ffffff;padding:10px 9px 8px;position:relative}
.tile-photo{display:block;width:110px;height:104px;margin:0 auto 8px}
.tile-title{font-size:11px;font-weight:600;color:var(--navy)}
.tile-store{font-size:8px;color:var(--muted);margin-top:2px}
.tile-comment{display:flex;align-items:center;gap:8px;margin-top:18px}
.avatar{width:18px;height:18px}
.comment-box{flex:1;height:17px;border:1px solid var(--input-border);border-radius:9px;font-size:7px;color:var(--muted);padding:3px 8px}
.tile-foot{display:flex;justify-content:space-between;align-items:flex-end;margin-top:12px}
.counters{font-size:7px;color:var(--muted)}
.price{font-size:16px;color:var(--price)}

/* Footer */
.site-footer{position:absolute;left:0;right:0;top:1044px;height:156px;background:linear-gradient(180deg,var(--footer-top),var(--footer-bot));color:var(--footer-text)}
.footer-search{position:absolute;left:39px;top:86px;display:flex}
.footer-search input{width:118px;height:24px;border:none;border-radius:2px 0 0 2px;font:inherit;font-size:9px;padding:0 6px}
.footer-search .search-btn{height:24px;width:28px}
.footer-col{position:absolute;top:22px}
.footer-col h2{font-size:10px;font-weight:700;color:#ffffff;letter-spacing:.3px;margin-bottom:10px}
.col-connect{left:232px;width:130px}
.col-browse{left:382px;width:150px}
.col-about{left:566px;width:185px}
.social{display:flex;align-items:center;gap:8px;font-size:8px;margin-bottom:9px}
.social-dot{width:14px;height:14px;border-radius:2px;background:var(--brand-blue)}
.social-dot.rss{background:#d98b2b}
.browse-list{list-style:none;font-size:8px}
.browse-list li{margin-bottom:8px}
.about-text{font-size:7px;line-height:1.45}
.copyright{font-size:7px;margin-top:6px;color:#ffffff}
</style>
</head>
<body>

<header class="site-header">
  <div class="brand">
    <div class="brand-mark"></div>
    <div>
      <div class="brand-name">zAntelope</div>
      <div class="brand-tagline">Local product search and discovery</div>
    </div>
  </div>
  <form class="header-search">
    <input type="text" aria-label="Search">
    <span class="search-btn"><svg width="13" height="13" viewBox="0 0 13 13"><circle cx="5.2" cy="5.2" r="4" fill="none" stroke="#fff" stroke-width="1.8"/><line x1="8.2" y1="8.2" x2="12" y2="12" stroke="#fff" stroke-width="2"/></svg></span>
  </form>
</header>

<nav class="main-nav">
  <a href="#" class="active">My profile</a>
  <a href="#">My Products</a>
  <a href="#">Add Product</a>
  <a href="#">Preview store</a>
</nav>

<section class="banner"><h1>Lorem Ipsum. Proin gravida nibh vel velit auctor</h1></section>

<main class="product-panel">
  <article class="tile"><div class="tile-photo" role="img" aria-label="Product photo: striped nightgown" style="background:linear-gradient(160deg,#e6e2e4,#9aa4b6)"></div><h3 class="tile-title">Striped Nightgown</h3><p class="tile-store">Main St Shop</p><div class="tile-comment"><svg class="avatar" viewBox="0 0 18 18"><circle cx="9" cy="6" r="4" fill="#3a4352"/><path d="M1 18c0-5 3.5-7 8-7s8 2 8 7z" fill="#3a4352"/></svg><div class="comment-box">What do you think?</div></div><div class="tile-foot"><span class="counters">0 Likes 0 Comments 0 Pods</span><span class="price">$100</span></div></article>

  <article class="tile"><div class="tile-photo" role="img" aria-label="Product photo: heated fleece scarf" style="background:linear-gradient(160deg,#e4dcd8,#8a5a5e)"></div><h3 class="tile-title">Heated Fleece scarf</h3><p class="tile-store">Main St Shop</p><div class="tile-comment"><svg class="avatar" viewBox="0 0 18 18"><circle cx="9" cy="6" r="4" fill="#3a4352"/><path d="M1 18c0-5 3.5-7 8-7s8 2 8 7z" fill="#3a4352"/></svg><div class="comment-box">What do you think?</div></div><div class="tile-foot"><span class="counters">0 Likes 0 Comments 0 Pods</span><span class="price">$60</span></div></article>

  <article class="tile"><div class="tile-photo" role="img" aria-label="Product photo: casual top" style="background:linear-gradient(160deg,#ece6e4,#a9444c)"></div><h3 class="tile-title">Casual top</h3><p class="tile-store">Main St Shop</p><div class="tile-comment"><svg class="avatar" viewBox="0 0 18 18"><circle cx="9" cy="6" r="4" fill="#3a4352"/><path d="M1 18c0-5 3.5-7 8-7s8 2 8 7z" fill="#3a4352"/></svg><div class="comment-box">What do you think?</div></div><div class="tile-foot"><span class="counters">0 Likes 0 Comments 0 Pods</span><span class="price">$58</span></div></article>

  <article class="tile"><div class="tile-photo" role="img" aria-label="Product photo: sweet sunflower candle" style="background:linear-gradient(160deg,#f1ede2,#c9b869)"></div><h3 class="tile-title">Sweet Sunflower Candle</h3><p class="tile-store">Main St Shop</p><div class="tile-comment"><svg class="avatar" viewBox="0 0 18 18"><circle cx="9" cy="6" r="4" fill="#3a4352"/><path d="M1 18c0-5 3.5-7 8-7s8 2 8 7z" fill="#3a4352"/></svg><div class="comment-box">What do you think?</div></div><div class="tile-foot"><span class="counters">0 Likes 0 Comments 0 Pods</span><span class="price">$30</span></div></article>

  <article class="tile"><div class="tile-photo" role="img" aria-label="Product photo: parrot corkscrew" style="background:linear-gradient(160deg,#f0f0f0,#4f7fa0)"></div><h3 class="tile-title">Parrot Corkscrew</h3><p class="tile-store">Main St Shop</p><div class="tile-comment"><svg class="avatar" viewBox="0 0 18 18"><circle cx="9" cy="6" r="4" fill="#3a4352"/><path d="M1 18c0-5 3.5-7 8-7s8 2 8 7z" fill="#3a4352"/></svg><div class="comment-box">What do you think?</div></div><div class="tile-foot"><span class="counters">0 Likes 0 Comments 0 Pods</span><span class="price">$62</span></div></article>

  <article class="tile"><div class="tile-photo" role="img" aria-label="Product photo: romantic print nightgown" style="background:linear-gradient(160deg,#eeeaec,#8a93b8)"></div><h3 class="tile-title">Romantic Print Nightgown</h3><p class="tile-store">Main St Shop</p><div class="tile-comment"><svg class="avatar" viewBox="0 0 18 18"><circle cx="9" cy="6" r="4" fill="#3a4352"/><path d="M1 18c0-5 3.5-7 8-7s8 2 8 7z" fill="#3a4352"/></svg><div class="comment-box">What do you think?</div></div><div class="tile-foot"><span class="counters">0 Likes 0 Comments 0 Pods</span><span class="price">$100</span></div></article>

  <article class="tile"><div class="tile-photo" role="img" aria-label="Product photo: insulated beverage holders" style="background:linear-gradient(160deg,#eef0f2,#6aa0b8)"></div><h3 class="tile-title">Insulated Beverage Holders</h3><p class="tile-store">Main St Shop</p><div class="tile-comment"><svg class="avatar" viewBox="0 0 18 18"><circle cx="9" cy="6" r="4" fill="#3a4352"/><path d="M1 18c0-5 3.5-7 8-7s8 2 8 7z" fill="#3a4352"/></svg><div class="comment-box">What do you think?</div></div><div class="tile-foot"><span class="counters">0 Likes 0 Comments 0 Pods</span><span class="price">$15</span></div></article>

  <article class="tile"><div class="tile-photo" role="img" aria-label="Product photo: cannella pyjamas" style="background:linear-gradient(160deg,#f0eeee,#a2b0c0)"></div><h3 class="tile-title">Cannella Pyjamas</h3><p class="tile-store">Main St Shop</p><div class="tile-comment"><svg class="avatar" viewBox="0 0 18 18"><circle cx="9" cy="6" r="4" fill="#3a4352"/><path d="M1 18c0-5 3.5-7 8-7s8 2 8 7z" fill="#3a4352"/></svg><div class="comment-box">What do you think?</div></div><div class="tile-foot"><span class="counters">0 Likes 0 Comments 0 Pods</span><span class="price">$180</span></div></article>

  <article class="tile"><div class="tile-photo" role="img" aria-label="Product photo: casual top" style="background:linear-gradient(160deg,#ece6e4,#a9444c)"></div><h3 class="tile-title">Casual top</h3><p class="tile-store">Main St Shop</p><div class="tile-comment"><svg class="avatar" viewBox="0 0 18 18"><circle cx="9" cy="6" r="4" fill="#3a4352"/><path d="M1 18c0-5 3.5-7 8-7s8 2 8 7z" fill="#3a4352"/></svg><div class="comment-box">What do you think?</div></div><div class="tile-foot"><span class="counters">0 Likes 0 Comments 0 Pods</span><span class="price">$58</span></div></article>

  <article class="tile"><div class="tile-photo" role="img" aria-label="Product photo: heated fleece scarf" style="background:linear-gradient(160deg,#f0eef0,#5a8fa8)"></div><h3 class="tile-title">Heated Fleece scarf</h3><p class="tile-store">Main St Shop</p><div class="tile-comment"><svg class="avatar" viewBox="0 0 18 18"><circle cx="9" cy="6" r="4" fill="#3a4352"/><path d="M1 18c0-5 3.5-7 8-7s8 2 8 7z" fill="#3a4352"/></svg><div class="comment-box">What do you think?</div></div><div class="tile-foot"><span class="counters">0 Likes 0 Comments 0 Pods</span><span class="price">$60</span></div></article>

  <article class="tile"><div class="tile-photo" role="img" aria-label="Product photo: striped nightgown" style="background:linear-gradient(160deg,#e8e6ea,#7b8aa8)"></div><h3 class="tile-title">Striped Nightgown</h3><p class="tile-store">Main St Shop</p><div class="tile-comment"><svg class="avatar" viewBox="0 0 18 18"><circle cx="9" cy="6" r="4" fill="#3a4352"/><path d="M1 18c0-5 3.5-7 8-7s8 2 8 7z" fill="#3a4352"/></svg><div class="comment-box">What do you think?</div></div><div class="tile-foot"><span class="counters">0 Likes 0 Comments 0 Pods</span><span class="price">$100</span></div></article>

  <article class="tile"><div class="tile-photo" role="img" aria-label="Product photo: emergency chocolate rations" style="background:linear-gradient(160deg,#e8dfe0,#8a2f3c)"></div><h3 class="tile-title">Emergency Chocolate Rations</h3><p class="tile-store">Main St Shop</p><div class="tile-comment"><svg class="avatar" viewBox="0 0 18 18"><circle cx="9" cy="6" r="4" fill="#3a4352"/><path d="M1 18c0-5 3.5-7 8-7s8 2 8 7z" fill="#3a4352"/></svg><div class="comment-box">What do you think?</div></div><div class="tile-foot"><span class="counters">0 Likes 0 Comments 0 Pods</span><span class="price">$5</span></div></article>
</main>

<footer class="site-footer">
  <form class="footer-search">
    <input type="text" aria-label="Search">
    <span class="search-btn"><svg width="12" height="12" viewBox="0 0 13 13"><circle cx="5.2" cy="5.2" r="4" fill="none" stroke="#fff" stroke-width="1.8"/><line x1="8.2" y1="8.2" x2="12" y2="12" stroke="#fff" stroke-width="2"/></svg></span>
  </form>

  <div class="footer-col col-connect">
    <h2>CONNECT WITH US</h2>
    <div class="social"><span class="social-dot"></span>Be a fan on Friendbook</div>
    <div class="social"><span class="social-dot"></span>Follow us on Chirper</div>
    <div class="social"><span class="social-dot rss"></span>RSS Feed</div>
  </div>

  <div class="footer-col col-browse">
    <h2>BROWSE</h2>
    <ul class="browse-list">
      <li>» Locations</li>
      <li>» Price Ranges</li>
      <li>» Categories</li>
      <li>» Featured Stores</li>
    </ul>
  </div>

  <div class="footer-col col-about">
    <h2>ABOUT ZANTELOPE</h2>
    <p class="about-text">zAntelope showcases beautiful products available at nearby retail stores. Browse the latest finds, follow the shops you love and save favourites into Pods so you can come back to them any time. Local owners add new products every day.</p>
    <p class="copyright">Copyright © zAntelope 2014. All rights reserved.</p>
  </div>
</footer>

</body>
</html>
```